Poster Design for Photography Exhibit

We are looking for a poster design for a photography exhibit featuring high-end fashion and celebrity photography.

Name of the exhibit is "MILES DORVAN: UNTITLED" (please use Helvetica Black all cap for show name.

Poster is LANDSCAPE format (2 units wide by 1 unit high).

Unfortunately due to legal reasons, we cannot use any actual Miles Dorvan photos. No can we use fashions or people on the poster!

We are looking for a high-end, sexy, bold provocative design that captures the excitement and glamour of a fashion photo shoot.

Target Market(s)

Men and Women interested in Fashion Photography and art photography in general

Industry/Entity Type

Fashion

Requirements
Must have
• landscape format, name of exhibit in Helvetica Black all caps
Nice to have
• Can be grayscale or color.
Should not have
• Logos or brand names

```html
<!DOCTYPE html>
<html lang="en">
<head>
<meta charset="utf-8">
<title>Miles Dorvan: Untitled — Photography Exhibit</title>
<link rel="stylesheet" href="https://fonts.googleapis.com/css2?family=Inter:wght@700;900&display=swap">
<style>
  :root {
    --paper: #ffffff;
    --ink: #1b1a1e;
    --frame: #2a2a2a;
    --red: #c8102e;
    --blue: #009fe0;
    --tripod-fade: #6b6a70;
  }
  html, body {
    margin: 0;
    padding: 0;
    width: 1200px;
    height: 1000px;
    overflow: hidden;
    background: var(--paper);
  }
  .poster {
    display: block;
    width: 1200px;
    height: 1000px;
  }
  .poster-frame {
    fill: var(--paper);
    stroke: var(--frame);
    stroke-width: 1.2;
  }
  .eyebrow {
    font-family: "Inter", Helvetica, Arial, sans-serif;
    font-weight: 700;
    font-size: 11.5px;
    letter-spacing: 2.6px;
    fill: var(--ink);
  }
  .show-name {
    font-family: "Inter", "Helvetica Neue", Helvetica, Arial, sans-serif;
    font-weight: 900;
    font-size: 114px;
    letter-spacing: -1px;
  }
  .show-name--first { fill: var(--red); }
  .show-name--last { fill: var(--blue); }
  .show-name--title { fill: var(--ink); }
</style>
</head>
<body>
<svg class="poster" viewBox="0 0 1200 1000" xmlns="http://www.w3.org/2000/svg">
  <defs>
    <linearGradient id="tripod-tone" x1="0" y1="0" x2="0" y2="1">
      <stop offset="0" stop-color="var(--ink)"/>
      <stop offset="1" stop-color="var(--tripod-fade)"/>
    </linearGradient>
  </defs>

  <rect class="poster-frame" x="50.5" y="227.5" width="1094" height="546"/>

  <text class="eyebrow" x="598" y="267" text-anchor="middle">PHOTOGRAPHY EXHIBIT</text>

  <rect class="tripod-area" role="img" aria-label="Camera tripod silhouette standing beneath the title"
        x="450" y="586" width="296" height="187" fill="url(#tripod-tone)"/>

  <text class="show-name show-name--first" x="597" y="410" text-anchor="middle">MILES</text>
  <text class="show-name show-name--last" x="599" y="495" text-anchor="middle">DORVAN</text>
  <text class="show-name show-name--title" x="597" y="583" text-anchor="middle">UNTITLED</text>
</svg>
</body>
</html>
```